brivox new business card design project

we need a new business card design. you can view info about us @ brivox.com. i have attached an example of our previous card with our previous name that we no longer use. We really liked the design, colors etc. look below to see more info about this project. it asks for a limited number of words. please see our website for more info about our compnay.

Target Market(s)

law enforcement

Contact Information for Business Card

i have uploaded an example of what we used before that we liked.

Font styles to use
Serif

```html
<!DOCTYPE html>
<html lang="en">
<head>
<meta charset="utf-8">
<title>Brivox business card</title>
<link rel="stylesheet" href="https://fonts.googleapis.com/css2?family=Open+Sans:wght@300;400;600&display=swap">
<style>
  :root{
    --page:#eceae6;
    --navy:#1b3a63;
    --navy-deep:#0f2546;
    --navy-light:#2c4f7c;
    --grey:#d3d5d9;
    --grey-dark:#b9bcc2;
    --teal:#2a93b0;
    --ink:#3a3f47;
    --white:#ffffff;
  }
  *{margin:0;padding:0;box-sizing:border-box}
  html,body{width:1200px;height:1200px;overflow:hidden;background:var(--page)}
  body{font-family:"Open Sans",Arial,sans-serif;position:relative}
  .card{position:absolute;left:140px;width:920px;height:526px;overflow:hidden;box-shadow:0 6px 18px rgba(0,0,0,.18)}
  .card--front{top:50px;background:var(--white)}
  .card--back{top:624px;background:var(--navy)}
  .card__art{position:absolute;inset:0}
  .wordmark{position:absolute;font-family:"Open Sans",Arial,sans-serif;font-weight:300;font-size:84px;letter-spacing:10px;line-height:1}
  .card--front .wordmark{left:220px;top:42px;color:var(--navy)}
  .card--back .wordmark{left:430px;top:150px;color:var(--white)}
  .address{position:absolute;left:44px;top:240px;color:var(--ink);font-size:19px;line-height:1.5}
  .address__line{display:flex;align-items:center;gap:10px}
  .address__line--indent{padding-left:0}
  .icon{width:20px;height:20px;flex:none}
  .person{position:absolute;right:60px;top:160px;text-align:right}
  .person__name{color:var(--teal);font-size:30px;font-weight:400;letter-spacing:1px}
  .person__role{color:var(--ink);font-size:18px;margin-top:2px}
  .contacts{position:absolute;right:60px;top:268px;list-style:none;color:var(--ink);font-size:19px;line-height:1.75}
  .contacts li{display:flex;align-items:center;justify-content:flex-end;gap:10px}
  .tagline{position:absolute;left:380px;top:430px;color:var(--ink);font-size:17px;letter-spacing:1px}
  .website{position:absolute;left:140px;top:330px;color:var(--white);font-size:24px;letter-spacing:1px}
</style>
</head>
<body>

<section class="card card--front" aria-label="Card front">
  <svg class="card__art" viewBox="0 0 920 526" aria-hidden="true">
    <defs>
      <linearGradient id="bandFront" x1="0" y1="0" x2="1" y2="0">
        <stop offset="0" stop-color="#0f2546"/>
        <stop offset="1" stop-color="#2c4f7c"/>
      </linearGradient>
      <linearGradient id="greyFront" x1="0" y1="0" x2="0" y2="1">
        <stop offset="0" stop-color="#c6c9ce"/>
        <stop offset="1" stop-color="#e1e3e6"/>
      </linearGradient>
      <filter id="softShadow" x="-10%" y="-10%" width="130%" height="130%">
        <feDropShadow dx="6" dy="4" stdDeviation="6" flood-opacity=".22"/>
      </filter>
    </defs>
    <polygon points="455,212 690,212 690,395 470,395" fill="url(#greyFront)" filter="url(#softShadow)"/>
    <polygon points="0,140 485,140 505,212 0,212" fill="url(#bandFront)"/>
  </svg>

  <div class="wordmark">BRIVOX</div>

  <div class="address">
    <div class="address__line">
      <svg class="icon" viewBox="0 0 20 20" aria-hidden="true"><rect width="20" height="20" rx="3" fill="#1b3a63"/><path d="M10 4a4 4 0 0 0-4 4c0 3 4 8 4 8s4-5 4-8a4 4 0 0 0-4-4zm0 5.5a1.5 1.5 0 1 1 0-3 1.5 1.5 0 0 1 0 3z" fill="#fff"/></svg>
      <span>2418 Harlow Avenue</span>
    </div>
    <div class="address__line address__line--indent">Austin, TX 78704</div>
  </div>

  <div class="person">
    <div class="person__name">DANIEL REYES</div>
    <div class="person__role">Creative Designer</div>
  </div>

  <ul class="contacts">
    <li>555.214.0377
      <svg class="icon" viewBox="0 0 20 20" aria-hidden="true"><rect width="20" height="20" rx="3" fill="#1b3a63"/><path d="M6 5h3l1 3-1.5 1a7 7 0 0 0 3 3L13 10.5l3 1v3c-6 .5-11-4.5-10-9.5z" fill="#fff"/></svg>
    </li>
    <li>www.brivox.com
      <svg class="icon" viewBox="0 0 20 20" aria-hidden="true"><rect width="20" height="20" rx="3" fill="#1b3a63"/><circle cx="10" cy="10" r="5.5" fill="none" stroke="#fff" stroke-width="1.3"/><path d="M4.5 10h11M10 4.5c-2.5 3-2.5 8 0 11M10 4.5c2.5 3 2.5 8 0 11" fill="none" stroke="#fff" stroke-width="1.1"/></svg>
    </li>
    <li>info@brivox.com
      <svg class="icon" viewBox="0 0 20 20" aria-hidden="true"><rect width="20" height="20" rx="3" fill="#1b3a63"/><rect x="4.5" y="6" width="11" height="8" fill="none" stroke="#fff" stroke-width="1.3"/><path d="M4.5 6l5.5 4.5L15.5 6" fill="none" stroke="#fff" stroke-width="1.3"/></svg>
    </li>
  </ul>

  <div class="tagline">LAW ENFORCEMENT INNOVATION</div>
</section>

<section class="card card--back" aria-label="Card back">
  <svg class="card__art" viewBox="0 0 920 526" aria-hidden="true">
    <defs>
      <radialGradient id="backGlow" cx=".6" cy=".45" r=".7">
        <stop offset="0" stop-color="#2c4f7c"/>
        <stop offset="1" stop-color="#132c52"/>
      </radialGradient>
      <linearGradient id="bandBack" x1="0" y1="0" x2="1" y2="0">
        <stop offset="0" stop-color="#0f2546"/>
        <stop offset="1" stop-color="#24446f"/>
      </linearGradient>
      <linearGradient id="greyBack" x1="0" y1="0" x2="0" y2="1">
        <stop offset="0" stop-color="#bfc2c8"/>
        <stop offset="1" stop-color="#dcdee1"/>
      </linearGradient>
    </defs>
    <rect width="920" height="526" fill="url(#backGlow)"/>
    <rect x="0" y="0" width="920" height="120" fill="#0f2546" opacity=".55"/>
    <polygon points="0,120 920,120 920,290 0,290" fill="url(#bandBack)" opacity=".35"/>
    <polygon points="560,290 920,290 920,440 578,440" fill="url(#greyBack)"/>
  </svg>

  <div class="wordmark">BRIVOX</div>
  <div class="website">www.brivox.com</div>
</section>

</body>
</html>
```